Awards Banquet Invitation

The Cedar Bluff Area Chamber of Commerce is celebrating it's 65th year at our Annual Awards Banquet (business leader awards). Since we were founded in 1950, we will have a 1950's theme. Dress will be 1950's Formal. I don't want cheesy 1950's. I want Classic feel and fonts from that era. This event is for business professionals so looks from ads in the 50's would be good for inspiration. I would like a look that I can use for the program and event ads. Invitation will include an RSVP insert. Date: February 10, 2015. Time: 6 cocktails, 7 dinner & program, Location: Holm Weide Country Club. Dress is 1950's formal

Target Market(s)

Business owners - our members

Industry/Entity Type

Business

Other font styles liked:
• Lasalle, linotype, thirsty

Colors
86cfc6
474747
ffffff
000000

Requirements
Must have
• classic 50's font and old-fashioned feel
Should not have
• sock hop, soda fountain, 50's diner

```html
<!DOCTYPE html>
<html lang="en">
<head>
<meta charset="UTF-8">
<title>Annual Awards Banquet Invitation</title>
<link rel="stylesheet" href="https://fonts.googleapis.com/css2?family=Lobster&family=Poiret+One&family=Bodoni+Moda:wght@700&display=swap">
<style>
  :root {
    --teal: #86cfc6;
    --teal-deep: #5f9d93;
    --teal-light: #a9ddd6;
    --glow: #eef0e6;
    --ink: #000000;
    --charcoal: #474747;
    --white: #ffffff;
  }
  html, body {
    margin: 0;
    padding: 0;
    overflow: hidden;
    background: var(--white);
  }
  .invitation {
    position: relative;
    width: 900px;
    height: 1200px;
    overflow: hidden;
    background: radial-gradient(ellipse 520px 520px at 450px 560px, var(--glow) 0%, var(--teal-light) 55%, var(--teal) 100%);
    color: var(--ink);
  }
  .damask-band {
    position: absolute;
    left: 0;
    width: 900px;
    background: linear-gradient(180deg, var(--teal-deep), #3f6f68 50%, var(--teal-deep));
  }
  .damask-band--top { top: 0; height: 152px; }
  .damask-band--bottom { top: 1010px; height: 190px; }
  .side-chevrons {
    position: absolute;
    left: 0;
    top: 0;
    width: 900px;
    height: 1200px;
  }
  .line {
    position: absolute;
    left: 0;
    width: 900px;
    text-align: center;
    margin: 0;
    white-space: nowrap;
  }
  .host {
    top: 172px;
    font-family: "Lobster", cursive;
    font-size: 42px;
  }
  .deco {
    font-family: "Poiret One", sans-serif;
  }
  .celebrating { top: 262px; font-size: 32px; }
  .anniversary { top: 298px; font-size: 96px; line-height: 1; }
  .lead-in { top: 410px; font-size: 24px; }
  .event-title {
    top: 470px;
    font-family: "Lobster", cursive;
    font-size: 86px;
    line-height: 80px;
  }
  .award-name {
    top: 666px;
    font-family: "Bodoni Moda", serif;
    font-weight: 700;
    font-size: 25px;
  }
  .date { top: 702px; font-size: 27px; }
  .time { top: 784px; font-size: 27px; line-height: 35px; }
  .location { top: 894px; font-size: 25px; }
  .dress-code { top: 953px; font-size: 36px; }
</style>
</head>
<body>
  <main class="invitation">
    <div class="damask-band damask-band--top" role="img" aria-label="Black and teal damask ornament pattern"></div>

    <svg class="side-chevrons" viewBox="0 0 900 1200" aria-hidden="true">
      <polygon points="0,405 170,548 0,692" fill="var(--ink)"/>
      <polygon points="0,458 108,548 0,638" fill="var(--teal-deep)" role="img" aria-label="Damask pattern inset"/>
      <polygon points="900,395 738,548 900,700" fill="var(--ink)"/>
      <polygon points="900,448 795,548 900,648" fill="var(--teal-deep)" role="img" aria-label="Damask pattern inset"/>
    </svg>

    <h2 class="line host">The Cedar Bluff Area Chamber of Commerce</h2>
    <p class="line deco celebrating">is celebrating it's</p>
    <p class="line deco anniversary">65th year</p>
    <p class="line deco lead-in">at our</p>
    <h1 class="line event-title">Annual Awards<br>Banquet</h1>
    <p class="line award-name">(Business Leader Awards)</p>
    <p class="line deco date">Date: February 10, 2015.</p>
    <p class="line deco time">Time: 6 o'clock Cocktails,<br>7 o'clock Dinner &amp; Program</p>
    <p class="line deco location">Location: Holm Weide Country Club</p>
    <p class="line deco dress-code">Dress Code is 1950's Formal</p>

    <div class="damask-band damask-band--bottom" role="img" aria-label="Black and teal damask ornament pattern"></div>
  </main>
</body>
</html>
```